Clean and modern business cards

Looking for an updated business card design for my dental office “corvanta dental” . Looking for a modern clean / sleek design . I’m thinking black background but open to seeing other options . One side needs to have an appointment card . Card needs to have logo, dentist name , phone, email , address . I’ve attached couple of cards I thought were cool as well as my logo
Target Market(s)
Dental patients
Industry/Entity Type
Dentistry
Contact Information for Business Card
Phone email address

```html
<!DOCTYPE html>
<html lang="en">
<head>
<meta charset="utf-8">
<title>Corvanta Dental – Business Card</title>
<link rel="stylesheet" href="https://fonts.googleapis.com/css2?family=Roboto:wght@300;400;500;700&display=swap">
<style>
  :root {
    --backdrop: #2a2a2a;
    --card: #1e1e1e;
    --ink: #f2f2f2;
    --ink-soft: #e6e6e6;
    --accent-gold: #d6a82c;
    --accent-red: #d8342a;
    --accent-green: #7db83a;
    --mark-tone: #1f8aa6;
  }
  html, body {
    margin: 0;
    padding: 0;
    width: 1200px;
    height: 900px;
    overflow: hidden;
    background: var(--backdrop);
    font-family: "Roboto", Arial, sans-serif;
  }
  .canvas {
    position: relative;
    width: 1200px;
    height: 900px;
  }
  .card {
    position: absolute;
    left: 384px;
    width: 430px;
    height: 246px;
    background: var(--card);
    box-shadow: 0 10px 24px rgba(0,0,0,0.45);
    color: var(--ink);
  }
  .card--front { top: 186px; }
  .card--back  { top: 468px; }

  /* Front */
  .brand {
    position: absolute;
    top: 46px;
    left: 0;
    right: 0;
    display: flex;
    justify-content: center;
    align-items: center;
    gap: 12px;
  }
  .brand__dot {
    width: 56px;
    height: 56px;
    border-radius: 50%;
    background: var(--mark-tone);
  }
  .brand__name {
    font-weight: 700;
    color: var(--ink);
    line-height: 1;
    text-align: right;
  }
  .brand__name-main {
    display: block;
    font-size: 23px;
    letter-spacing: 0.5px;
  }
  .brand__name-sub {
    display: block;
    font-size: 9px;
    letter-spacing: 4.5px;
    margin-top: 4px;
  }
  .contact {
    position: absolute;
    left: 0;
    right: 0;
    text-align: center;
    font-weight: 300;
    font-size: 12.5px;
    color: var(--ink-soft);
    margin: 0;
    white-space: nowrap;
  }
  .contact--name  { top: 140px; }
  .contact--phone { top: 159px; }
  .contact--address { top: 190px; }
  .contact--web  { top: 205px; }
  .label--gold  { color: var(--accent-gold); }
  .label--red   { color: var(--accent-red); }
  .label--green { color: var(--accent-green); }

  /* Back */
  .back-mark {
    position: absolute;
    left: 15px;
    top: 53px;
    width: 136px;
    height: 136px;
    border-radius: 50%;
    background: var(--mark-tone);
  }
  .appointment__title {
    position: absolute;
    top: 49px;
    left: 182px;
    width: 198px;
    text-align: center;
    font-weight: 300;
    font-size: 12.5px;
    margin: 0;
  }
  .appointment__field {
    position: absolute;
    left: 182px;
    width: 198px;
    border-top: 1px solid var(--ink-soft);
    text-align: center;
    font-weight: 300;
    font-size: 12.5px;
    padding-top: 6px;
  }
  .appointment__field--date { top: 92px; }
  .appointment__field--time { top: 134px; }
  .appointment__policy {
    position: absolute;
    top: 194px;
    left: 140px;
    width: 276px;
    text-align: center;
    font-weight: 500;
    font-size: 12px;
    line-height: 15px;
    margin: 0;
  }
</style>
</head>
<body>
<main class="canvas">
  <section class="card card--front" aria-label="Card front">
    <div class="brand">
      <span class="brand__dot"></span>
      <span class="brand__name">
        <span class="brand__name-main">CORVANTA</span>
        <span class="brand__name-sub">DENTAL</span>
      </span>
    </div>
    <p class="contact contact--name">Dr. Helena Varoski</p>
    <p class="contact contact--phone">(204) 555-0193</p>
    <p class="contact contact--address"><span class="label--gold">Address:</span> 820 Larchmont Ave, Winnipeg, MB</p>
    <p class="contact contact--web"><span class="label--red">Email:</span> hello@corvantadental.ca | <span class="label--green">Website:</span> corvantadental.ca</p>
  </section>

  <section class="card card--back" aria-label="Appointment card">
    <div class="back-mark"></div>
    <p class="appointment__title">Your Next Appointment is:</p>
    <div class="appointment__field appointment__field--date">Date</div>
    <div class="appointment__field appointment__field--time">Time</div>
    <p class="appointment__policy">To cancel or reschedule please notify us at least 48 hours prior to your scheduled appointment</p>
  </section>
</main>
</body>
</html>
```